Design a website for our "Bright Motion" Initiative we are implementing at our Youth Soccer Club.

We need a web design for a wellness initiative for our soccer club. "Bright Motion" is the program title. The website will have health and wellness content related to our initiative. It should have interactive features for our users. Videos, survey/data submission capabilities, etc. Colors themed to align with logo. see my start of a website at www.brightmotionwithtown.com. I like the homepage design, the rest is unprofessional looking. Design should provide education, tips, advice, resources, for health & wellness; wellness related to our pillars. 6 tabs in addition to home page: Drink more water, fuel your performance, stretch more, protect your skin more, move more, and sports mindset. (year 2 diagram wheel). Sports counseling will be next big focus. Wordpress based website. Easy for me to update in the future.

Target Market(s)

Families with children participating in soccer. concept also applicable to other youth sports.

Industry/Entity Type

Health And Wellness

Number of Pages Required

5+ page

Font styles to use
Sans Serif

Colors
0292cd
f37122

Requirements
Must have
• Bright Motion Logo
• Marlowe Brook Soccer Club Logo (*updated*)
• Home page
• Video included that is currently on the website homepage www.brightmotionwithtown.com
• Page for each of the 6 pillars
• Focus on "drink more water" pillar and "Mindset" (will focus on sports counseling)
• Flexibility for me to update/edit the website moving forward (non-coding).
• User friendly graphic/picture interface
Nice to have
• Design focused more on the themes, not on soccer. Want the design to be applicable to parents and youth of all sports. Education and interactive features to all ages.

```html
<!DOCTYPE html>
<html lang="en">
<head>
<meta charset="utf-8">
<title>Bright Motion</title>
<link href="https://fonts.googleapis.com/css2?family=Roboto:wght@300;400;500;700&family=Roboto+Condensed:wght@400;700&display=swap" rel="stylesheet">
<style>
:root{
  --teal:#12778a;
  --teal-light:#1a9bb0;
  --orange:#f37122;
  --ink:#333333;
  --muted:#666666;
  --ring:#e2e2e2;
  --footer:#2a2a2a;
  --footer-line:#444444;
  --white:#ffffff;
}
*{margin:0;padding:0;box-sizing:border-box}
html,body{width:1200px;height:2695px;overflow:hidden;background:var(--white)}
body{position:relative;font-family:"Roboto",Arial,sans-serif;color:var(--ink)}
.abs{position:absolute}

/* header */
.site-header{left:0;top:0;width:1200px;height:118px;background:var(--white)}
.brand{left:70px;top:18px;display:flex;flex-direction:column;align-items:center;gap:8px}
.brand-mark{width:46px;height:46px;border-radius:50%;background:var(--orange)}
.brand-name{font-family:"Roboto Condensed",sans-serif;font-weight:700;font-size:17px;color:var(--teal);letter-spacing:.5px}
.social-top{left:836px;top:22px;display:flex;gap:12px}
.social-dot{width:26px;height:26px;border-radius:50%;background:#222}
.club-name{left:1005px;top:16px;width:130px;font-family:"Roboto Condensed",sans-serif;font-weight:700;font-size:15px;line-height:16px;color:#222;text-align:center;text-transform:uppercase}
.main-nav{left:266px;top:79px;width:934px;height:39px;background:var(--teal);display:flex;align-items:center}
.main-nav a{font-family:"Roboto Condensed",sans-serif;font-weight:700;font-size:17px;color:var(--white);text-decoration:none;padding:0 21px;height:39px;line-height:39px}
.main-nav a.active{background:var(--orange);padding:0 26px}

/* hero */
.hero{left:0;top:118px;width:1200px;height:579px;background:radial-gradient(ellipse at 60% 45%,#e9d2bf 0%,#c9a489 18%,#9fbf4a 42%,#79b431 70%,#5e9a25 100%)}
.hero-title{left:160px;top:318px;font-weight:300;font-size:47px;line-height:44px;color:#111}
.hero-title span{display:block}
.hero-title .l2{padding-left:52px}
.hero-title .l3{padding-left:22px}
.slider-dots{left:1093px;top:348px;width:30px;height:90px;border-radius:15px;background:rgba(255,255,255,.55);display:flex;flex-direction:column;align-items:center;justify-content:center;gap:8px}
.slider-dots i{width:14px;height:14px;border-radius:50%;background:#cfd9c2}
.slider-dots i.on{background:var(--teal)}

/* promo banners */
.promos{left:0;top:700px;width:1200px;height:195px}
.promo-text{position:absolute;top:42px;width:470px;text-align:center;color:var(--white)}
.promo-text h2{font-family:"Roboto Condensed",sans-serif;font-weight:700;font-size:36px;line-height:38px;text-transform:uppercase}
.promo-text p{font-size:14.5px;line-height:21px;margin-top:6px}
.promo-btn{display:inline-block;margin-top:12px;padding:6px 12px;font-family:"Roboto Condensed",sans-serif;font-weight:700;font-size:14px;color:var(--white)}
.promo-left{left:75px}
.promo-left .promo-btn{background:var(--teal)}
.promo-right{left:655px}
.promo-right .promo-btn{background:var(--orange)}
.promo-badge{left:553px;top:763px;width:90px;height:90px;border-radius:50%;background:var(--white);border:3px solid var(--teal);display:flex;align-items:center;justify-content:center}
.promo-badge i{width:34px;height:34px;border-radius:50%;background:var(--orange)}

/* welcome */
.welcome-title{left:115px;top:958px;width:430px;text-align:center;font-family:"Roboto Condensed",sans-serif;font-size:34px;color:var(--orange)}
.welcome-title strong{color:var(--teal);font-weight:700}
.welcome-rule{left:270px;top:1012px;width:120px;height:20px}
.welcome-copy{left:84px;top:1050px;width:492px;font-size:14.5px;line-height:26px;color:var(--muted);text-align:center}
.video{left:86px;top:1288px;width:485px;height:309px;background:#111;border:4px solid #e8e8e8}
.video-frame{position:absolute;left:0;top:0;width:477px;height:270px;background:linear-gradient(180deg,#1b1b1b 0%,#2e3b2a 40%,#3f6a2f 70%,#2f5a25 100%)}
.wheel{left:610px;top:1000px;width:540px;height:590px}

/* feature tiles */
.tile{top:1706px;height:341px;display:flex;align-items:center;justify-content:center;text-align:center}
.tile h3{font-family:"Roboto Condensed",sans-serif;font-weight:700;font-size:28px;line-height:29px;color:var(--white);text-transform:uppercase}
.tile-hydration{left:0;width:395px;background:linear-gradient(135deg,#5d6a4e 0%,#8a8f76 45%,#b3ae9c 100%)}
.tile-color{left:402px;width:395px;background:radial-gradient(ellipse at 50% 50%,#7a5a3e 0%,#6b4a30 45%,#5a6a2e 80%,#8a3a2a 100%)}
.tile-fuel{left:805px;width:395px;background:linear-gradient(90deg,#9a9a9a 0%,#c6c0b8 45%,#d7a867 75%,#b9c06a 100%)}

/* partners */
.partners{left:171px;top:2132px;width:804px;height:153px;border:2px solid #eeeeee;background:var(--white)}
.partner{position:absolute;top:16px;height:117px;width:242px;display:flex;align-items:center;justify-content:center;text-align:center;background:#f2f2f2}
.partner-lead{left:20px;background:var(--teal);color:var(--white);font-size:33px;line-height:34px;font-weight:400}
.partner-club{left:280px;font-family:"Roboto Condensed",sans-serif;font-weight:700;font-size:22px;line-height:25px;color:#222}
.partner-foundation{left:542px;font-family:"Roboto Condensed",sans-serif;font-weight:700;font-size:22px;line-height:25px;color:var(--teal-light)}

/* footer */
.site-footer{left:0;top:2362px;width:1200px;height:333px;background:var(--footer);color:#dddddd}
.footer-col{position:absolute;top:50px;width:240px}
.footer-col h4{font-family:"Roboto Condensed",sans-serif;font-weight:700;font-size:19px;line-height:23px;color:var(--white);padding-bottom:12px;border-bottom:1px solid var(--footer-line);margin-bottom:16px}
.footer-col li{font-size:14px;line-height:26px;list-style:none}
.footer-col p{font-size:14px;line-height:22px}
.footer-col .gap-phone{margin-top:18px}
.footer-col .gap-email{margin-top:10px}
.footer-social{display:flex;gap:12px}
.footer-social .social-dot{background:#dddddd;width:24px;height:24px}
.field{height:36px;border:1px solid #666;margin-bottom:18px;font-size:13px;line-height:34px;padding-left:10px;color:#dddddd}
.subscribe{height:40px;background:var(--orange);color:var(--white);font-family:"Roboto Condensed",sans-serif;font-weight:700;font-size:17px;text-align:center;line-height:40px}
.copyright{left:72px;top:2651px;font-size:14px;color:#dddddd}
.footer-rule{left:72px;top:2636px;width:1056px;height:1px;background:var(--footer-line)}
</style>
</head>
<body>

<header class="site-header abs">
  <div class="brand abs"><span class="brand-mark"></span><span class="brand-name">BRIGHT MOTION</span></div>
  <div class="social-top abs"><span class="social-dot"></span><span class="social-dot"></span><span class="social-dot"></span><span class="social-dot"></span></div>
  <div class="club-name abs">Marlowe Brook Soccer Club</div>
</header>
<nav class="main-nav abs">
  <a class="active" href="#">HOME</a>
  <a href="#">WATER</a>
  <a href="#">FRUITS &amp; VEGETABLES</a>
  <a href="#">STRETCH</a>
  <a href="#">FUEL YOUR BODY</a>
  <a href="#">PROTECT YOUR SKIN</a>
</nav>

<section class="hero abs" role="img" aria-label="Child drinking a glass of water against a green background"></section>
<h1 class="hero-title abs"><span>Drink</span><span class="l2">More</span><span class="l3">Water</span></h1>
<div class="slider-dots abs"><i class="on"></i><i></i><i></i></div>

<section class="promos abs">
  <svg width="1200" height="195" viewBox="0 0 1200 195" aria-hidden="true">
    <defs>
      <linearGradient id="promoOrange" x1="0" x2="1"><stop offset="0" stop-color="#c9651f"/><stop offset=".35" stop-color="#f37122"/><stop offset="1" stop-color="#f37122"/></linearGradient>
      <linearGradient id="promoTeal" x1="0" x2="1"><stop offset="0" stop-color="#1a9bb0"/><stop offset=".7" stop-color="#1a93a8"/><stop offset="1" stop-color="#2d7f8f"/></linearGradient>
    </defs>
    <polygon points="0,0 618,0 583,195 0,195" fill="url(#promoOrange)"/>
    <polygon points="618,0 1200,0 1200,195 583,195" fill="url(#promoTeal)"/>
    <line x1="618" y1="0" x2="583" y2="195" stroke="#ffffff" stroke-width="5"/>
  </svg>
  <div class="promo-text promo-left">
    <h2>Drink More Water</h2>
    <p>Lorem ipsum dolor sit amet, consectetur adipiscing elit, sed do eiusmod tempor incididunt ut labore et dolore magna aliqua.</p>
    <span class="promo-btn">READ MORE ›</span>
  </div>
  <div class="promo-text promo-right">
    <h2>Sports Mindset</h2>
    <p>Lorem ipsum dolor sit amet, consectetur adipiscing elit, sed do eiusmod tempor incididunt ut labore et dolore magna aliqua.</p>
    <span class="promo-btn">READ MORE ›</span>
  </div>
</section>
<div class="promo-badge abs"><i></i></div>

<h2 class="welcome-title abs">WELCOME TO <strong>BRIGHT MOTION</strong></h2>
<svg class="welcome-rule abs" viewBox="0 0 120 20" aria-hidden="true">
  <line x1="0" y1="10" x2="48" y2="10" stroke="#cccccc"/>
  <circle cx="60" cy="10" r="6" fill="#f37122"/>
  <line x1="72" y1="10" x2="120" y2="10" stroke="#cccccc"/>
</svg>
<p class="welcome-copy abs">Bright Motion is a partnership between Marlowe Brook Soccer Club and the Summit Ridge Foundation. It is an initiative to help communities develop attitudes and skills to make consistent and positive health-related choices. Promote healthy child development through involvement in sports, building a sense of well-being and meeting the growth, development, and activity needs of healthy, confident children and young people. A health and wellness initiative that will educate and provide resources to the players and their families in Marlowe Brook Soccer Club.</p>
<div class="video abs"><div class="video-frame" role="img" aria-label="Video still of young players on a floodlit soccer field at night"></div></div>

<svg class="wheel abs" viewBox="0 0 540 590" font-family="Roboto Condensed, sans-serif" font-weight="700" font-size="17" fill="#ffffff" text-anchor="middle">
  <circle cx="265" cy="329" r="235" fill="none" stroke="#e2e2e2" stroke-width="2"/>
  <text x="265" y="336" fill="#12778a" font-size="26">BRIGHT MOTION</text>
  <g>
    <circle cx="265" cy="69" r="59" fill="#12778a"/>
    <text x="265" y="54">DRINK</text><text x="265" y="73">MORE</text><text x="265" y="92">WATER</text>
  </g>
  <g>
    <circle cx="453" cy="180" r="59" fill="#12778a"/>
    <text x="453" y="165">FUEL</text><text x="453" y="184">YOUR</text><text x="453" y="203">BODY</text>
  </g>
  <g>
    <circle cx="453" cy="410" r="59" fill="#12778a"/>
    <text x="453" y="405">STRETCH</text><text x="453" y="424">MORE</text>
  </g>
  <g>
    <circle cx="265" cy="521" r="59" fill="#12778a"/>
    <text x="265" y="506">PROTECT</text><text x="265" y="525">YOUR</text><text x="265" y="544">SKIN</text>
  </g>
  <g>
    <circle cx="74" cy="410" r="59" fill="#12778a"/>
    <text x="74" y="405">MOVE</text><text x="74" y="424">MORE</text>
  </g>
  <g>
    <circle cx="74" cy="180" r="59" fill="#12778a"/>
    <text x="74" y="175">SPORTS</text><text x="74" y="194">MINDSET</text>
  </g>
</svg>

<article class="tile tile-hydration abs" role="img" aria-label="Woman drinking a glass of water"><h3>Performance<br>and Hydration</h3></article>
<article class="tile tile-color abs" role="img" aria-label="Colourful vegetables arranged around a wooden board"><h3>Boost Performance<br>by Adding Color</h3></article>
<article class="tile tile-fuel abs" role="img" aria-label="Woman in sportswear beside a plate of fruit and vegetables"><h3>Fuel Your<br>Performance</h3></article>

<section class="partners abs">
  <div class="partner partner-lead">A<br>PARTNERSHIP</div>
  <div class="partner partner-club">MARLOWE BROOK<br>SOCCER CLUB</div>
  <div class="partner partner-foundation">SUMMIT RIDGE<br>FOUNDATION</div>
</section>

<footer class="site-footer abs">
  <div class="footer-col" style="left:72px">
    <h4>QUICK LINKS</h4>
    <ul><li>Home</li><li>Water</li><li>Fruits &amp; Vegetables</li><li>Stretch</li><li>Fuel Your Body</li><li>Protect Your Skin</li></ul>
  </div>
  <div class="footer-col" style="left:343px">
    <h4>CONTACT US</h4>
    <p>Bright Motion<br>Lorem ipsum dolor, DR 29492</p>
    <p class="gap-phone">Phone<br>(100) 000-0000</p>
    <p class="gap-email">Email<br>info@brightmotionwithtown.com</p>
  </div>
  <div class="footer-col" style="left:612px">
    <h4>FOLLOW US ON</h4>
    <div class="footer-social"><span class="social-dot"></span><span class="social-dot"></span><span class="social-dot"></span><span class="social-dot"></span></div>
  </div>
  <div class="footer-col" style="left:882px">
    <h4>NEWSLETTER SIGN UP</h4>
    <div class="field">Name</div>
    <div class="field">Email</div>
    <div class="subscribe">SUBSCRIBE NOW</div>
  </div>
</footer>
<div class="footer-rule abs"></div>
<p class="copyright abs">© 2017 Bright Motion.</p>

</body>
</html>
```